Landing page for a cyber security service provider called 'Lumen Grove'

The client is a new cyber security company in need of a website landing page at lumengrove.example.

Their visual identity is modern, playful, clean and uncluttered and represents innovation, connectivity and approachability.

The company logo is provided in black (attached) but the client is open to changing the colour to align with the new website design.

The landing page needs to contain:
- A call to action with a 'Get Started' button
-Links to blank 'How it works', 'Products', 'Pricing', 'About Us' and 'Contact Us' pages (that we'll fill out later)

Target Market(s)

Medium to large businesses who probably don't understand cyber / cyber security but need their business to be protected.

Industry/Entity Type

Cyber Security

Coding

Coded - Design and coding required

Number of Pages Required

1 page

Font styles to use
Sans Serif
Other font styles liked:
• Helvetica

Requirements
Nice to have
• Hero banner at the top of the landing page.
Should not have
• Should not look like a traditional cyber / cyber security design (eg no dark blue/ black, red/black colour combinations). Please no military styles (eg no shields, cannons, swords, guns)

```html
<!DOCTYPE html>
<html lang="en">
<head>
<meta charset="utf-8">
<title>Lumen Grove — Cybersecurity Solutions</title>
<link rel="stylesheet" href="https://fonts.googleapis.com/css2?family=Poppins:wght@300;700&family=Inter:wght@400;600&display=swap">
<style>
  :root {
    --white: #ffffff;
    --ink: #1d1b2e;
    --teal: #12a89a;
    --violet: #7a55e6;
    --coral: #ff7a6b;
    --mint: #8ff0dd;
    --footer: #5b3fc4;
  }
  * { margin: 0; padding: 0; box-sizing: border-box; }
  html, body { width: 1200px; height: 648px; overflow: hidden; }
  body { font-family: "Inter", "Helvetica Neue", Helvetica, Arial, sans-serif; background: var(--white); position: relative; }

  .site-header { position: absolute; left: 0; top: 0; width: 1200px; height: 85px; background: var(--white); }
  .brand { position: absolute; left: 141px; top: 30px; display: flex; align-items: center; gap: 7px;
    font-size: 16px; font-weight: 600; color: var(--ink); text-decoration: none; }
  .brand-dot { width: 10px; height: 10px; border-radius: 50%; background: var(--teal); }
  .main-nav { position: absolute; left: 346px; top: 34px; display: flex; gap: 33px; }
  .main-nav a { font-size: 13px; color: var(--ink); text-decoration: none; white-space: nowrap; }
  .main-nav a.is-active { font-weight: 600; color: var(--violet); }
  .btn { position: absolute; display: flex; align-items: center; justify-content: center; gap: 7px;
    border-radius: 30px; font-size: 13px; letter-spacing: 0.3px; text-decoration: none; }
  .btn svg { width: 18px; height: 12px; }
  .btn-header { left: 896px; top: 21px; width: 163px; height: 43px; background: var(--violet); color: var(--white); }

  .hero { position: absolute; left: 0; top: 85px; width: 1200px; height: 529px; overflow: hidden;
    background: linear-gradient(120deg, var(--teal) 0%, #2b8fd6 45%, var(--violet) 100%); }
  .hero-visual { position: absolute; left: 0; top: 0; width: 720px; height: 529px;
    background:
      radial-gradient(ellipse 180px 190px at 326px 190px, rgba(200,255,245,0.7), rgba(143,240,221,0.3) 60%, transparent 100%),
      radial-gradient(ellipse 260px 140px at 326px 470px, rgba(255,255,255,0.6), rgba(143,240,221,0.3) 55%, transparent 100%); }
  .hero-copy { position: absolute; left: 683px; top: 116px; width: 440px; color: var(--white); }
  .hero-title { font-family: "Poppins", "Helvetica Neue", Arial, sans-serif; font-size: 45px; line-height: 50px;
    font-weight: 300; letter-spacing: 0.2px; }
  .hero-title strong { font-weight: 700; }
  .hero-lede { margin-top: 7px; font-size: 14.5px; line-height: 27px; width: 370px; }
  .btn-hero { left: 683px; top: 367px; width: 162px; height: 42px; background: var(--white); color: var(--ink); }

  .site-footer { position: absolute; left: 0; top: 614px; width: 1200px; height: 34px; background: var(--footer);
    color: var(--white); font-size: 12.5px; display: flex; align-items: center; justify-content: center; }
</style>
</head>
<body>
  <header class="site-header">
    <a class="brand" href="#"><span class="brand-dot"></span>Lumen Grove</a>
    <nav class="main-nav">
      <a class="is-active" href="#">Home</a>
      <a href="#">How it works</a>
      <a href="#">About Us</a>
      <a href="#">Products</a>
      <a href="#">Pricing</a>
      <a href="#">Contact us</a>
    </nav>
    <a class="btn btn-header" href="#">GET STARTED
      <svg viewBox="0 0 18 12" fill="none" stroke="currentColor" stroke-width="2"><path d="M0 6h16M11 1l5 5-5 5"/></svg>
    </a>
  </header>

  <section class="hero">
    <div class="hero-visual" role="img" aria-label="Glowing digital network illustration above a circuit pathway"></div>
    <div class="hero-copy">
      <h1 class="hero-title"><strong>CYBERSECURITY<br>SOLUTIONS</strong> FOR<br>YOUR BUSINESS</h1>
      <p class="hero-lede">Protect your people, network, devices, and data from internal and external threats with Lumen Grove IT security solutions.</p>
    </div>
    <a class="btn btn-hero" href="#">GET STARTED
      <svg viewBox="0 0 18 12" fill="none" stroke="currentColor" stroke-width="2"><path d="M0 6h16M11 1l5 5-5 5"/></svg>
    </a>
  </section>

  <footer class="site-footer">© 2024 LUMEN GROVE. ALL RIGHTS RESERVED</footer>
</body>
</html>
```